Screendesign für neue Website
Zielgruppe
Bauherren und alle die mal zum Architekten müssen.
Aufgabenstellung
Bei diesem Auftrag handelt es sich um die Erstellung eines Screendesigns für eine Website eines Archtiktenbüros.
Es wird daher ein Layout im PSD-Format erwartet, eine Umsetzung dessen in HTML wird nicht gefordert.

```html
<!DOCTYPE html>
<html lang="de">
<head>
<meta charset="utf-8">
<title>Hausfeld Architekten – Screendesign</title>
<link rel="stylesheet" href="https://fonts.googleapis.com/css2?family=Share+Tech+Mono&family=Quicksand:wght@400&display=swap">
<style>
  :root {
    --stage: #8a8a8a;
    --frame: #2f2e2f;
    --topbar: #2a292a;
    --main: #2d2c2d;
    --band: #232223;
    --menu: #343334;
    --menu-line: #272627;
    --text-light: #d8d8d8;
    --text-dark: #111111;
    --menu-text: #b9b9b9;
    --logo-bg: #ffffff;
    --logo-ink: #1a1a1a;
    --logo-accent: #4caf2a;
  }
  * { margin: 0; padding: 0; box-sizing: border-box; }
  html, body { width: 1200px; height: 821px; overflow: hidden; }
  body { background: var(--stage); position: relative; }

  .site {
    position: absolute; left: 40px; top: 60px; width: 1120px; height: 700px;
    background: var(--frame); border-radius: 8px; overflow: hidden;
  }
  .site__topbar { position: absolute; left: 0; top: 0; width: 100%; height: 50px; background: var(--topbar); }

  .gallery { position: absolute; left: 0; top: 50px; width: 100%; height: 100px; background: #1d1c1d; }
  .gallery__photo { position: absolute; top: 0; height: 100px; }

  .stage-main { position: absolute; left: 0; top: 150px; width: 100%; height: 438px; background: var(--main); }

  .claim { position: absolute; left: 3px; font-family: "Share Tech Mono", monospace; font-size: 31px;
    letter-spacing: 4px; text-align: right; padding-right: 12px; line-height: 43px; height: 43px; background: var(--band); }
  .claim--light { color: var(--text-light); }
  .claim--dark { color: var(--text-dark); }

  .brand { position: absolute; left: 3px; top: 454px; width: 368px; height: 106px; background: var(--logo-bg);
    display: flex; align-items: center; justify-content: center; gap: 12px; }
  .brand__mark { width: 22px; height: 22px; background: var(--logo-accent); }
  .brand__name { font-family: "Share Tech Mono", monospace; font-size: 22px; color: var(--logo-ink); letter-spacing: 1px; }

  .nav { position: absolute; left: 749px; top: 150px; width: 182px; height: 438px; list-style: none; }
  .nav__item { height: 73px; background: var(--menu); border-bottom: 2px solid var(--menu-line);
    display: flex; align-items: center; justify-content: center;
    font-family: "Quicksand", sans-serif; font-size: 18px; color: var(--menu-text); }
  .nav__item:last-child { border-bottom: none; }

  .floor { position: absolute; left: 0; top: 588px; width: 100%; height: 112px;
    background: linear-gradient(180deg, #1c1b1c 0%, #3a3a3a 18%, #353535 100%); }
  .floor::before { content: ""; position: absolute; left: 0; top: -22px; width: 100%; height: 22px;
    background: linear-gradient(180deg, rgba(0,0,0,0), rgba(0,0,0,0.45)); }
</style>
</head>
<body>
  <main class="site">
    <div class="site__topbar"></div>

    <div class="gallery">
      <div class="gallery__photo" style="left:3px;width:183px;background:linear-gradient(180deg,#9fb4c9 0%,#8a5a48 55%,#4f7a3a 100%)" role="img" aria-label="Foto: Backsteinhaus mit rotem Dach und Garten"></div>
      <div class="gallery__photo" style="left:189px;width:182px;background:linear-gradient(180deg,#dfe3e6 0%,#7c7f82 50%,#4f6a3c 100%)" role="img" aria-label="Foto: Helles Einfamilienhaus mit Garten"></div>
      <div class="gallery__photo" style="left:374px;width:183px;background:linear-gradient(180deg,#e9ecef 0%,#5c6066 55%,#6f7a5a 100%)" role="img" aria-label="Foto: Weißes Haus mit dunklem Dach"></div>
      <div class="gallery__photo" style="left:560px;width:182px;background:radial-gradient(circle at 50% 55%,#b0442e 0%,#6b4a32 45%,#2b2622 100%)" role="img" aria-label="Foto: Beleuchteter Innenraum mit Holzdecke"></div>
      <div class="gallery__photo" style="left:746px;width:182px;background:linear-gradient(180deg,#5d6f8c 0%,#c9a766 50%,#4b4a3e 100%)" role="img" aria-label="Foto: Mehrfamilienhaus in Abendsonne"></div>
      <div class="gallery__photo" style="left:931px;width:186px;background:linear-gradient(180deg,#6f93c4 0%,#8e4a3c 55%,#5a5a5a 100%)" role="img" aria-label="Foto: Backstein-Stadthaus an einer Straße"></div>
    </div>

    <section class="stage-main">
      <div class="nav-spacer"></div>
    </section>

    <p class="claim claim--light" style="top:242px;width:538px">ARCHITEKTEN SCHAFFEN</p>
    <p class="claim claim--dark" style="top:295px;width:465px">LEBENS-RAUM</p>
    <p class="claim claim--light" style="top:347px;width:602px">LEBENS-TRAUM</p>
    <p class="claim claim--dark" style="top:400px;width:675px;height:45px">TRAUM HAUS</p>

    <div class="brand">
      <span class="brand__mark"></span>
      <span class="brand__name">Hausfeld Architekten</span>
    </div>

    <ul class="nav">
      <li class="nav__item">Unternehmen</li>
      <li class="nav__item">Projekte</li>
      <li class="nav__item">Information</li>
      <li class="nav__item">Aktuelles</li>
      <li class="nav__item">Leistungen</li>
      <li class="nav__item">Kontakt</li>
    </ul>

    <div class="floor" role="img" aria-label="Dunkle Holzdielen-Textur als Fußbereich"></div>
  </main>
</body>
</html>
```